Business card design for sports medicine and athlete care clinic.

We need a bold, solid business card design for our practitioners to stand out. We treat overuse & sports-related injuries and provide post-operative rehabilitation. Our specialisations include chronic conditions, men’s health, nutrition & musculoskeletal disorders (MSDs). All brand collateral in terms of fonts, logo and colour palette to be provided.

Target Market(s)

Athletes (professional and amateur), sportspeople, predominantly male

Industry/Entity Type

Health And Wellness

Contact Information for Business Card

The front of the card should be white with dark blue text the back dark blue with white text. The logo should be top-left. The business name should be horizontal and right of the logo. The tagline should be directly below centred on the back of the card (see top-banner.png and bottom-banner.png)

Font styles to use
Sans Serif

Colors
0355a3
0293ce
3176b5
ffffff
85acd3

Requirements
Nice to have
• Diagonal and/or horizontal line elements between logo and practitioner details and/or bottom corner of card (see slide.png and tag-bg.png).

```html
<!DOCTYPE html>
<html lang="en">
<head>
<meta charset="utf-8">
<title>Stride Collective — Business Card</title>
<link rel="stylesheet" href="https://fonts.googleapis.com/css2?family=Roboto:ital,wght@0,300;0,400;0,500;0,700;1,500&display=swap">
<style>
  :root {
    --navy: #0d0b3b;
    --navy-deep: #03022a;
    --sky: #1b98d5;
    --mark-blue: #0293ce;
    --muted-title: #4b4d7a;
    --paper: #ffffff;
    --canvas: #ffffff;
  }
  * { margin: 0; padding: 0; box-sizing: border-box; }
  html, body {
    width: 1200px; height: 1200px; overflow: hidden;
    background: var(--canvas);
    font-family: "Roboto", Arial, sans-serif;
  }
  .stage { position: relative; width: 1200px; height: 1200px; }

  .card {
    position: absolute;
    box-shadow: 0 18px 34px rgba(0,0,0,0.28);
    overflow: hidden;
  }
  .card-front {
    left: 305px; top: 173px; width: 532px; height: 338px;
    background: var(--paper);
    border-radius: 22px 0 22px 0;
    border-bottom: 7px solid var(--navy);
  }
  .card-back {
    left: 296px; top: 661px; width: 552px; height: 352px;
    background: var(--navy-deep);
    border-radius: 24px 0 24px 0;
  }

  .brand-mark {
    position: absolute;
    border-radius: 50%;
    background: var(--mark-blue);
  }
  .card-front .brand-mark { left: 32px; top: 14px; width: 92px; height: 92px; }
  .card-back .brand-mark { left: 30px; top: 82px; width: 118px; height: 118px; }

  .brand-name {
    position: absolute; white-space: nowrap;
    font-weight: 700; line-height: 1;
  }
  .card-front .brand-name { left: 166px; top: 52px; font-size: 40px; color: var(--navy); }
  .card-back .brand-name { left: 177px; top: 117px; font-size: 38px; font-weight: 400; color: var(--muted-title); }

  .tagline {
    position: absolute; white-space: nowrap;
    font-style: italic; font-weight: 500; line-height: 1;
    color: var(--sky);
  }
  .card-front .tagline { left: 166px; top: 98px; font-size: 20px; }
  .card-back .tagline { left: 169px; top: 173px; font-size: 21px; }

  .person-name {
    position: absolute; left: 251px; top: 142px;
    font-size: 36px; font-weight: 400; color: var(--navy); line-height: 1;
  }
  .person-role {
    position: absolute; left: 251px; top: 183px;
    font-size: 17px; font-weight: 300; color: var(--navy); line-height: 1;
  }
  .section-label {
    position: absolute; white-space: nowrap;
    font-size: 19px; font-weight: 400; color: var(--sky); line-height: 1;
  }
  .details-label { left: 251px; top: 214px; }
  .address-label { left: 29px; top: 202px; }
  .details-rule {
    position: absolute; left: 251px; top: 234px; width: 277px; height: 3px;
    background: var(--navy);
  }
  .contact-list, .address-lines {
    position: absolute; list-style: none;
    font-size: 12.5px; color: var(--navy); line-height: 1;
  }
  .contact-list { left: 251px; top: 0; }
  .contact-list li { position: absolute; left: 0; white-space: nowrap; }
  .contact-list .email { top: 246px; }
  .contact-list .phone-a { top: 267px; }
  .contact-list .phone-b { top: 288px; }
  .contact-list .web { top: 306px; }
  .address-lines { left: 29px; top: 231px; }
  .address-lines li { margin-bottom: 7px; white-space: nowrap; }

  .social-row { position: absolute; left: 29px; top: 277px; display: flex; gap: 14px; }
  .social-slot {
    width: 27px; height: 27px; border-radius: 6px;
    background: var(--mark-blue);
  }
</style>
</head>
<body>
<main class="stage">
  <section class="card card-front" aria-label="Business card front">
    <span class="brand-mark" aria-hidden="true"></span>
    <h1 class="brand-name">Stride Collective</h1>
    <p class="tagline">Sports medicine and athlete care</p>

    <h2 class="person-name">Marcus Elden</h2>
    <p class="person-role">Executive Director</p>

    <h3 class="section-label details-label">Contact Details</h3>
    <div class="details-rule"></div>
    <ul class="contact-list">
      <li class="email">stridecollective@mail.com</li>
      <li class="phone-a">555.214.3390 2</li>
      <li class="phone-b">555-214-3392 5</li>
      <li class="web">www.stridecollective.com.au</li>
    </ul>

    <h3 class="section-label address-label">Contact&nbsp; Address</h3>
    <ul class="address-lines">
      <li>418 W. Alder Rd #210</li>
      <li>Carson, NV 89701</li>
    </ul>
    <div class="social-row" aria-label="Social profiles">
      <span class="social-slot"></span>
      <span class="social-slot"></span>
      <span class="social-slot"></span>
      <span class="social-slot"></span>
    </div>
  </section>

  <section class="card card-back" aria-label="Business card back">
    <span class="brand-mark" aria-hidden="true"></span>
    <h1 class="brand-name">Stride Collective</h1>
    <p class="tagline">Sports medicine and athlete care</p>
  </section>
</main>
</body>
</html>
```